Open for over 30 years, we are finally looking to bottle and sell our homemade hot sauce. We are looking for a label that will serve as the future of hot sauce wherever we open more Corvallo's. The current choice for the name is "The Blaze over Corvallo" (a play on words with the song) but we are open to other names and ideas.

www.corvallonyc.com

Industry/Entity Type

Restaurant

Colors
0255a3
fbed22

```html
<!DOCTYPE html>
<html lang="en">
<head>
<meta charset="utf-8">
<title>The Blaze over Corvallo — Hot Sauce Label</title>
<link rel="stylesheet" href="https://fonts.googleapis.com/css2?family=Fredoka:wght@600&family=Josefin+Sans:wght@300;400&family=Lobster+Two:ital,wght@1,700&family=PT+Sans+Narrow&display=swap">
<style>
  :root {
    --page: #ffffff;
    --label-yellow: #f2e650;
    --sauce-blue: #1f6fb6;
    --sauce-blue-deep: #2165ab;
    --headline-yellow: #fbed22;
    --name-yellow: #fcd65c;
    --rule-grey: #c9d3dc;
    --volume-ink: #2e3134;
  }
  * { margin: 0; padding: 0; box-sizing: border-box; }
  html, body {
    width: 835px;
    height: 1200px;
    overflow: hidden;
    background: var(--page);
  }
  .label {
    position: absolute;
    left: 45px;
    top: 37px;
    width: 741px;
    height: 1113px;
    background: var(--label-yellow);
    box-shadow: 2px 3px 6px rgba(0, 0, 0, 0.25);
  }
  .label-field {
    position: absolute;
    left: 19px;
    top: 19px;
    right: 19px;
    bottom: 19px;
    overflow: hidden;
    background: linear-gradient(180deg, var(--sauce-blue) 0%, var(--sauce-blue-deep) 50%, var(--sauce-blue) 100%);
  }
  .label-content {
    background: none;
  }
  .headline {
    position: absolute;
    left: 0;
    top: 250px;
    width: 100%;
    text-align: center;
    font-family: "Fredoka", sans-serif;
    font-weight: 600;
    font-size: 56px;
    letter-spacing: 1px;
    color: var(--headline-yellow);
    line-height: 1;
  }
  .name-frame {
    position: absolute;
    left: 43px;
    top: 327px;
    width: 616px;
    height: 165px;
    border: 12px solid var(--name-yellow);
    display: flex;
    align-items: center;
    justify-content: center;
    overflow: hidden;
  }
  .name {
    font-family: "Josefin Sans", sans-serif;
    font-weight: 300;
    font-size: 84px;
    letter-spacing: 14px;
    margin-right: -14px;
    color: var(--name-yellow);
    line-height: 1;
    padding-top: 12px;
    white-space: nowrap;
  }
  .since {
    position: absolute;
    left: 37px;
    top: 565px;
    width: 630px;
    display: flex;
    align-items: center;
    gap: 28px;
  }
  .since-rule {
    flex: 1;
    height: 2px;
    background: var(--rule-grey);
  }
  .since-text {
    font-family: "Lobster Two", cursive;
    font-style: italic;
    font-weight: 700;
    font-size: 32px;
    color: var(--headline-yellow);
    line-height: 1;
  }
  .volume {
    position: absolute;
    left: 0;
    bottom: 35px;
    width: 100%;
    text-align: center;
    font-family: "PT Sans Narrow", sans-serif;
    font-size: 34px;
    color: var(--volume-ink);
  }
</style>
</head>
<body>
  <div class="label">
    <div class="label-field" role="img" aria-label="Background of blue wave pattern in the style of a seaside promenade pavement"></div>
    <div class="label-field label-content">
      <h1 class="headline">THE BLAZE OVER</h1>
      <div class="name-frame">
        <span class="name">CORVALLO</span>
      </div>
      <div class="since">
        <span class="since-rule"></span>
        <span class="since-text">since 1979</span>
        <span class="since-rule"></span>
      </div>
      <p class="volume">250ml</p>
    </div>
  </div>
</body>
</html>
```